Professional BIO Template with photo and logo

Hello,
I need a professional Bio template developed via Microsoft WORD ASAP!!!!! I would like to just be able to add the text I need to add. So resize-able text boxes. Potentially able to adjust the font. These are the things I need added it to include.
Head shot (attached)
Text Box for Name
Text Box for phone number
Text box for email
KTW Logo (attached)
Maybe a blue banner at the top or some background boxes that are blue or grey. Here are the pantone colors that our company uses.

CORE COLOR
100c 91m 17y 6k 38r 58g 128b Hex #263A80 Pantone 7687 C

CORE CONTRAST COLOR
36c 29m 28y 0k 168r 168g 170b Hex #669999 Pantone Cool Gray 6C

I also attached some examples of what we have been looking at. Instead of green add the blue...instead of black maybe just be white.

Thank you

```html
<!DOCTYPE html>
<html lang="en">
<head>
<meta charset="utf-8">
<title>Daniel Hartley – Bio</title>
<link rel="stylesheet" href="https://fonts.googleapis.com/css2?family=Arimo:ital,wght@0,400;0,700;1,400&family=Roboto+Condensed:wght@400&family=Tinos:ital@1&display=swap">
<style>
  :root {
    --navy: #2f3c82;
    --navy-text: #313f88;
    --sky: #bfdff4;
    --pale: #e3f0fb;
    --grey: #c0c0c0;
    --ink: #333333;
    --page-bg: #ecedef;
    --white: #ffffff;
  }
  * { margin: 0; padding: 0; box-sizing: border-box; }
  html, body { width: 1039px; height: 1200px; overflow: hidden; background: var(--page-bg); }
  .stage { position: relative; width: 1039px; height: 1200px; }
  .sheet {
    position: absolute; left: 71px; top: 20px;
    width: 1264px; height: 1634px;
    transform: scale(0.71); transform-origin: 0 0;
    background: var(--white);
    box-shadow: 0 6px 24px rgba(0,0,0,.18);
    overflow: hidden;
    font-family: "Arimo", Arial, sans-serif;
  }
  .abs { position: absolute; }
  .top-band { left: 0; top: 0; width: 1264px; height: 128px; background: var(--navy); }
  .sky-band { left: 0; top: 128px; width: 1264px; height: 188px; background: var(--sky); }
  .header-visual {
    left: 600px; top: 0; width: 664px; height: 316px;
    background: linear-gradient(100deg, rgba(255,255,255,0) 0%, rgba(120,150,210,.35) 45%, rgba(70,100,180,.45) 75%, rgba(150,190,235,.5) 100%);
  }
  .side-column {
    left: 0; top: 316px; width: 343px; height: 1318px;
    background: linear-gradient(to bottom, var(--white) 0%, var(--white) 8%, var(--pale) 100%);
  }
  .portrait-ring {
    left: 26px; top: 54px; width: 336px; height: 336px; border-radius: 50%;
    background: var(--white);
  }
  .portrait {
    left: 38px; top: 66px; width: 312px; height: 312px; border-radius: 50%;
    background: radial-gradient(circle at 50% 40%, #d9a58a 0%, #b98068 22%, #4a4a4a 48%, #3a3a3a 100%);
  }
  .website {
    left: 908px; top: 46px; display: flex; align-items: center; gap: 14px;
    color: var(--white); font-family: "Roboto Condensed", Arial, sans-serif; font-size: 25px;
  }
  .name {
    left: 421px; top: 180px; font-size: 52px; font-weight: 700; color: var(--navy-text); letter-spacing: .2px;
  }
  .role {
    left: 424px; top: 240px; font-family: "Tinos", "Times New Roman", serif; font-style: italic;
    font-size: 50px; color: #2c2c3a;
  }
  .side-summary {
    left: 46px; top: 428px; width: 280px;
    font-family: "Tinos", "Times New Roman", serif; font-style: italic; font-size: 22px; line-height: 25.2px;
    color: var(--navy-text);
  }
  .brand-mark {
    left: 46px; top: 1300px; width: 252px; height: 204px;
    display: flex; align-items: center; justify-content: center;
    font-size: 64px; font-weight: 700; color: var(--navy-text); letter-spacing: 4px;
  }
  .main { left: 421px; top: 424px; width: 770px; color: var(--ink); }
  .section-title { font-size: 36px; line-height: 41px; font-weight: 400; color: var(--navy-text); margin-bottom: 26px; }
  .main p { font-size: 19.5px; line-height: 23px; padding-left: 3px; }
  .role-title { font-size: 19.5px; font-weight: 700; color: var(--navy-text); margin: 25px 0 10px 3px; }
  .duties { list-style: none; }
  .duties li { position: relative; padding-left: 39px; font-size: 19.5px; line-height: 23px; margin-bottom: 12px; }
  .duties li::before {
    content: ""; position: absolute; left: 5px; top: 6px; width: 11px; height: 11px; border-radius: 50%; background: #222;
  }
  .footer-grey { left: 0; top: 1530px; width: 343px; height: 70px; background: var(--grey); }
  .footer-bar { left: 343px; top: 1530px; width: 921px; height: 70px; background: var(--navy); }
  .contact {
    top: 1548px; display: flex; align-items: center; gap: 14px;
    color: var(--white); font-family: "Roboto Condensed", Arial, sans-serif; font-size: 27px;
  }
  .contact.phone { left: 458px; }
  .contact.email { left: 866px; }
</style>
</head>
<body>
<div class="stage">
  <div class="sheet">
    <div class="abs top-band"></div>
    <div class="abs sky-band"></div>
    <div class="abs header-visual" role="img" aria-label="Photo of glass office towers seen from below"></div>
    <div class="abs side-column"></div>

    <div class="abs portrait-ring"></div>
    <div class="abs portrait" role="img" aria-label="Head shot of Daniel Hartley"></div>

    <div class="abs website">
      <svg width="32" height="32" viewBox="0 0 32 32" fill="none" stroke="#fff" stroke-width="2">
        <circle cx="16" cy="16" r="14"/><ellipse cx="16" cy="16" rx="6" ry="14"/>
        <line x1="2" y1="16" x2="30" y2="16"/><path d="M5 9h22M5 23h22"/>
      </svg>
      <span>www.yourwebsite.com</span>
    </div>

    <h1 class="abs name">Daniel Hartley Textboxname</h1>
    <div class="abs role">Marketing Executive</div>

    <p class="abs side-summary">Lorem ipsum dolor sit amet, consectetur adipiscing aalit. Quisque varius, mi sedabboa sedcondim entum graaaavid a, ligula nunc maximus orci, sit amet mollis odio turpaaa is et maris. Crasddd tempor mattis dictum. Vivaus interdu mdiam inlor emkkajjik moll is, atakjis tincdunt nullaak tab varius.aik Aliquam ut co ngquam. Seded pretium riee dsf ngillabibendumaa sadaa cursus. Sed id ligula sadsdw necasasa magna lacinia asd laoreet. Etiam id temporeee velit. Phasellus sed doloreee tincidunt, elementusam diam gravida, pharetra eros. wxa Aenean diam dolor, laoreet ut lectus eu, eleifeaswed.</p>

    <div class="abs brand-mark">KTW</div>

    <section class="abs main">
      <h2 class="section-title">PROFESSIONAL<br>EXPERIENCES</h2>
      <p>Lorem ipsum dolor sit amet, consectetur adipiscing elit. Quisque varius, mi sed condimentum gravida, ligula nunc maximus orci, sit amet mollis odio turpis et mauris. Cras tempor mattis dictum. Vivamus interdum diam in lorem mollis, at tincidunt nulla varius. Aliquam ut congue quam. Sed pretium fringilla orci bibendum cursus. Sed id ligula nec magna lacinia laoreet. Etiam id tempor velit. Phasellus sed dolor tincidunt, elementum diam gravida, pharetra eros. Aenean diam dolor, laoreet ut lectus eu, eleifend varius urna. Etiam dictum ipsum quis hendrerit iaculis. Sed ut semper quam, sed consequat tortor. Curabitur ornare mollis eleifend. Quisque sem sem, efficitur luctus eros a, semper consequat arcu. Proin vel posuere quam, ut ultrices libero.</p>

      <h3 class="role-title">Lorem ipsum dolor sit amet, consectetur</h3>
      <ul class="duties">
        <li>Phasellus facilisis, nibh sed vestibulum semper, arcu turpis pellentesque est, eu mollis sem elit ac diam.</li>
        <li>In dictum velit eget nisl finibus euismod. Mauris aliquet finibus felis, ac vehicula quam maximus vitae. Maecenas ac dui eget elit tempor blandit auctor a lectus. Curabitur quis libero eu sem pretium placerat.</li>
        <li>Quisque maximus ligula velit, sit amet varius nisl interdum vel. Duis a ullamcorper massa, a pulvinar ante. Vivamus finibus odio sed ligula eleifend ullamcorper. Vivamus a iaculis diam. Aenean luctus dui in nunc sodales scelerisque.</li>
        <li>Phasellus tellus sem, egestas at erat quis, tincidunt fringilla nisi. Cras ultricies volutpat tortor.</li>
      </ul>

      <h3 class="role-title">Lorem ipsum dolor sit amet, consectetur</h3>
      <ul class="duties">
        <li>Phasellus facilisis, nibh sed vestibulum semper, arcu turpis pellentesque est, eu mollis sem elit ac diam.</li>
        <li>In dictum velit eget nisl finibus euismod. Mauris aliquet finibus felis, ac vehicula quam maximus vitae. Maecenas ac dui eget elit tempor blandit auctor a lectus. Curabitur quis libero eu sem pretium placerat.</li>
        <li>Quisque maximus ligula velit, sit amet varius nisl interdum vel. Duis a ullamcorper massa, a pulvinar ante. Vivamus finibus odio sed ligula eleifend ullamcorper. Vivamus a iaculis diam. Aenean luctus dui in nunc sodales scelerisque.</li>
        <li>Phasellus tellus sem, egestas at erat quis, tincidunt fringilla nisi. Cras ultricies volutpat tortor.</li>
      </ul>
    </section>

    <div class="abs footer-grey"></div>
    <div class="abs footer-bar"></div>
    <div class="abs contact phone">
      <svg width="36" height="36" viewBox="0 0 36 36">
        <circle cx="18" cy="18" r="18" fill="#fff"/>
        <path d="M12 9c1-1 2-1 3 0l2 3c.6 1 .3 1.8-.5 2.5l-1 1c1 2.5 3 4.5 5.5 5.5l1-1c.7-.8 1.5-1.1 2.5-.5l3 2c1 1 1 2 0 3l-1.5 1.5c-2 2-9-1-13-5s-7-11-5-13z" fill="#2f3c82"/>
      </svg>
      <span>0012-3456-5678</span>
    </div>
    <div class="abs contact email">
      <svg width="36" height="36" viewBox="0 0 36 36">
        <circle cx="18" cy="18" r="18" fill="#fff"/>
        <rect x="9" y="12" width="18" height="12" fill="none" stroke="#2f3c82" stroke-width="2"/>
        <path d="M9 12l9 7 9-7M9 24l6-6M27 24l-6-6" fill="none" stroke="#2f3c82" stroke-width="2"/>
      </svg>
      <span>support@yourwebsite.com</span>
    </div>
  </div>
</div>
</body>
</html>
```